IT Professional business card with a hometown feel and a little edgy.

My business name is Pebble Website Solutions. But I have ended up doing much more. I live in a very small remote community, where everyone knows everyone. We like the one-on-one customer service in this community. I do computer tutoring, virus removal, networking, and software training. My clients are businesses and private individuals.

My website is pebblewebsitesolutions.example, when I first designed it I was going for a fresh, clean look, which I still like. But I am thinking about making the website a bit more edgy to match my new logo from ArtGrovely (logo attached). At this time my website does not display the new logo, but I plan on redesigning the website in the future to match the logo and business card.

My tag line is "put the web to work for you"

I'm thinking I would like to have the business card printed with a metallic finish.

Please do not use black backgrounds, or any solid dark colors. Prefer light or white backgrounds.

Target Market(s)

Small businesses. Individuals that need computer help at home.

Industry/Entity Type

It Company

Contact Information for Business Card

Marla Dunovan
Pebble Website Solutions
PO Box 7153
Alder Creek, WA 98399
Cell: 360-555-0172
marla@pebblewebsitesolutions.example
pebblewebsitesolutions.example

Font styles to use
Serif

Requirements
Must have
• Must have all the information listed in "Business Card Details"
• Must use the logo provided.
• Use the colors from the provided logo
Nice to have
• Would like to use my tagline "put the web to work for you" all lowercase

```html
<!DOCTYPE html>
<html lang="en">
<head>
<meta charset="utf-8">
<title>Pebble Website Solutions – Business Card</title>
<link rel="stylesheet" href="https://fonts.googleapis.com/css2?family=Open+Sans:wght@400;600&display=swap">
<style>
  :root {
    --canvas: #ecebe8;
    --card: #fbfbfb;
    --card-edge: #e2e2e2;
    --ink: #3b3b3b;
    --ink-soft: #5a5a5a;
    --green: #3f9a3a;
    --green-dark: #2a7a2a;
    --green-light: #8cc97f;
    --rule: #8a8a8a;
  }
  * { box-sizing: border-box; margin: 0; padding: 0; }
  html, body {
    width: 1200px; height: 780px; overflow: hidden;
    background: var(--canvas);
    font-family: "Open Sans", Arial, sans-serif;
  }
  .sheet { position: relative; width: 1200px; height: 780px; }
  .card {
    position: absolute; top: 236px;
    width: 540px; height: 308px;
    background: linear-gradient(160deg, #ffffff 0%, var(--card) 55%, #f1f1f1 100%);
    border: 1px solid var(--card-edge);
    box-shadow: 0 10px 24px rgba(0,0,0,0.12);
    overflow: hidden;
  }
  .card--front { left: 40px; }
  .card--back { left: 620px; }

  /* Front */
  .front-art { position: absolute; inset: 0; }
  .company-name {
    position: absolute; left: 28px; top: 26px;
    font-size: 24px; font-weight: 400; color: var(--ink);
  }
  .person-name {
    position: absolute; left: 176px; top: 64px;
    font-size: 24px; font-weight: 400; color: var(--green);
  }
  .address {
    position: absolute; right: 26px; top: 104px;
    font-style: normal; text-align: right;
    font-size: 13px; line-height: 19px; color: var(--ink);
  }
  .address .line { display: flex; justify-content: flex-end; align-items: center; gap: 6px; }
  .icon-box { display: inline-block; width: 13px; height: 13px; background: var(--green); }
  .contact-row {
    position: absolute; left: 24px; right: 24px; top: 190px;
    display: flex; justify-content: space-between; align-items: baseline;
    font-size: 11.5px; white-space: nowrap;
  }
  .email { color: var(--ink); }
  .website { color: var(--green); }

  /* Back */
  .brand {
    position: absolute; left: 118px; top: 92px;
    display: flex; align-items: center; gap: 22px;
  }
  .brand-mark { width: 84px; height: 84px; background: var(--green); }
  .brand-rule { width: 1px; height: 96px; background: var(--rule); }
  .brand-name { font-size: 23px; line-height: 26px; font-weight: 600; color: var(--green); }
  .tagline {
    position: absolute; left: 118px; top: 206px;
    font-size: 15px; letter-spacing: 3.4px; color: var(--ink-soft);
  }
</style>
</head>
<body>
<main class="sheet">

  <section class="card card--front" aria-label="Business card front">
    <svg class="front-art" width="540" height="308" viewBox="0 0 540 308">
      <defs>
        <linearGradient id="photoTone" x1="0" y1="0" x2="1" y2="1">
          <stop offset="0" stop-color="#c9d3da"/>
          <stop offset="0.5" stop-color="#6e6a66"/>
          <stop offset="1" stop-color="#9aa29c"/>
        </linearGradient>
        <linearGradient id="swoosh" x1="0" y1="0" x2="1" y2="0">
          <stop offset="0" stop-color="var(--green-light)"/>
          <stop offset="1" stop-color="var(--green-dark)"/>
        </linearGradient>
      </defs>
      <path d="M0 222 C 170 220, 360 228, 540 246 L540 308 L0 308 Z" fill="url(#swoosh)"/>
      <path role="img" aria-label="Portrait photo of Marla Dunovan by the shore"
            d="M0 230 C 170 228, 360 238, 540 258 L540 308 L0 308 Z" fill="url(#photoTone)"/>
    </svg>
    <h1 class="company-name">Pebble Website Solutions</h1>
    <p class="person-name">Marla Dunovan</p>
    <address class="address">
      <span class="line">PO Box 7153</span>
      <span class="line">Alder Creek, WA 98399</span>
      <span class="line">360-555-0172 <span class="icon-box" aria-hidden="true"></span></span>
      <span class="line">pebblewebsitesolutions <span class="icon-box" aria-hidden="true"></span></span>
    </address>
    <div class="contact-row">
      <span class="email">marla@pebblewebsitesolutions.example</span>
      <span class="website">www.pebblewebsitesolutions.example</span>
    </div>
  </section>

  <section class="card card--back" aria-label="Business card back">
    <div class="brand">
      <span class="brand-mark" aria-hidden="true"></span>
      <span class="brand-rule" aria-hidden="true"></span>
      <p class="brand-name">Pebble<br>Website<br>Solutions</p>
    </div>
    <p class="tagline">put the web to work for you</p>
  </section>

</main>
</body>
</html>
```